Bramblecrest Apparel and Nutrition is looking for a Clothing/Supplement Online Store Website!

Must be convenient, and user friendly, with vibrant colors that catch the eye!

Target Market(s)

Athletes, and Fashion Customers

Industry/Entity Type

Fitness

Coding

Coded - Design and coding required

Number of Pages Required

3 page

Font styles to use
Decorative

Colors

Designer to choose colors to be used in the design.

Requirements
Must have
• Somewhere to feature products, features to promote discounts and make announcements.
Nice to have
• My logos on each page

```html
<!DOCTYPE html>
<html lang="en">
<head>
<meta charset="utf-8">
<title>Bramblecrest Apparel and Nutrition</title>
<link href="https://fonts.googleapis.com/css2?family=Montserrat:wght@400;500;600;700;800;900&display=swap" rel="stylesheet">
<style>
:root{
  --ink:#1b1b1b;
  --ink-2:#262626;
  --lime:#a3ef0a;
  --orange:#ff9a00;
  --coral:#f8524d;
  --mist:#e4e9eb;
  --paper:#ffffff;
  --news-bg:#efefef;
  --muted:#777777;
  --line:#d9d9d9;
}
*{box-sizing:border-box;margin:0;padding:0}
html,body{width:1200px;height:4714px;overflow:hidden}
body{position:relative;background:var(--paper);font-family:"Montserrat",Arial,sans-serif;color:var(--ink)}
.abs{position:absolute}
.photo{position:absolute}

/* header + hero */
.hero-bg{position:absolute;left:0;top:0;width:1200px;height:1175px}
.site-header{position:absolute;left:0;top:0;width:1200px;height:68px;border-bottom:1px dashed rgba(255,255,255,.25)}
.brand{position:absolute;left:93px;top:16px;color:#fff;font-weight:800;font-size:30px;letter-spacing:1px;display:flex;align-items:center;gap:10px}
.brand .dot{width:14px;height:14px;background:var(--lime)}
.main-nav{position:absolute;top:26px;left:569px;display:flex;font-size:12px;font-weight:500;color:#fff}
.main-nav span{position:absolute;white-space:nowrap}
.hero-title{position:absolute;left:93px;top:288px;color:#fff;font-weight:800;font-size:62px;letter-spacing:1px;line-height:1;white-space:nowrap}
.hero-sub{position:absolute;left:93px;top:366px;color:#fff;font-weight:500;font-size:38px;white-space:nowrap}
.btn-skew{position:absolute;display:flex;align-items:center;justify-content:center;font-weight:700;font-size:14px}
.btn-skew::before{content:"";position:absolute;inset:0;transform:skewX(-30deg);border:2px solid var(--lime);border-top-color:rgba(255,255,255,.5);border-right-color:rgba(255,255,255,.5)}
.btn-skew span{position:relative}
.btn-lime{color:var(--lime)}
.btn-dark{color:var(--ink)}
.btn-dark::before{border-color:var(--lime);border-top-color:#cfcfcf;border-right-color:#cfcfcf}
.btn-white{color:#fff;font-size:13px}
.btn-white::before{border-color:#fff}

.promo{position:absolute;color:#fff;text-align:center}
.promo-top{left:419px;top:690px;width:362px;height:228px;background:var(--orange)}
.promo-sale{left:419px;top:942px;width:362px;height:228px;background:var(--coral)}
.promo h2{font-weight:800;line-height:1}
.promo-top h2{font-size:52px;margin-top:36px}
.promo-top h3{font-size:21px;font-weight:700;margin-top:6px}
.promo-top p{font-size:13px;margin-top:6px}
.promo-sale h2{font-size:54px;margin-top:38px}

/* sections */
.section-title{position:absolute;width:100%;text-align:center;font-weight:800;font-size:31px;color:var(--ink);letter-spacing:.5px;white-space:nowrap;line-height:1.2}
.section-title.compact{font-size:28px;letter-spacing:0}
.section-text{position:absolute;text-align:center;font-size:11px;line-height:18px;color:var(--muted)}
.pager{position:absolute;display:flex;gap:8px}
.pager svg{width:22px;height:22px}

/* product card */
.card{position:absolute;border:1px solid #cfcfcf;background:#fff;text-align:center}
.card-mark{position:absolute;left:20px;top:20px;width:22px;height:22px;background:#555}
.card-tools{position:absolute;right:18px;top:16px;display:flex;flex-direction:column;gap:10px}
.card-tools svg{width:18px;height:18px}
.card-img{position:absolute;left:50%;transform:translateX(-50%)}
.stars{position:absolute;left:0;width:100%;color:var(--orange);letter-spacing:3px}
.card-name{position:absolute;left:0;width:100%;font-weight:600;color:var(--ink);white-space:nowrap}
.price{position:absolute;left:0;width:100%;font-weight:700;color:#76c000}
.price s{color:#999;font-weight:500}
.card-desc{position:absolute;left:0;width:100%;color:#555;white-space:nowrap}
.card .btn-skew{left:50%;transform:translateX(-50%)}

.card-lg{width:324px;height:421px}
.card-lg .card-img{top:20px;width:220px;height:215px}
.card-lg .stars{top:240px;font-size:17px}
.card-lg .card-name{top:272px;font-size:14px}
.card-lg .price{top:290px;font-size:27px}
.card-lg .price s{font-size:14px}
.card-lg .card-desc{top:324px;font-size:11.5px}
.card-lg .btn-skew{top:352px;width:140px;height:34px}

.card-sm{width:243px;height:320px}
.card-sm .card-mark{left:16px;top:16px;width:18px;height:18px}
.card-sm .card-tools{right:12px;top:10px;gap:6px}
.card-sm .card-tools svg{width:15px;height:15px}
.card-sm .card-img{top:30px;width:150px;height:140px}
.card-sm .stars{top:178px;font-size:12px}
.card-sm .card-name{top:200px;font-size:11px}
.card-sm .price{top:214px;font-size:20px}
.card-sm .price s{font-size:10px}
.card-sm .card-desc{top:242px;font-size:9px}
.card-sm .btn-skew{top:262px;width:105px;height:26px;font-size:11px}

.tabs{position:absolute;font-size:11.5px;color:#999;white-space:nowrap}
.tabs b{color:#6fbf00;font-weight:500}
.tabs i{font-style:normal;margin:0 12px}

/* band */
.deal-band{position:absolute;left:0;top:2314px;width:1200px;height:338px}
.band-text{position:absolute;left:93px;top:2388px;color:#fff;font-weight:600;font-size:26px;line-height:26px;white-space:nowrap}
.band-big{position:absolute;left:91px;top:2452px;color:var(--lime);font-weight:800;font-size:52px;white-space:nowrap}

/* features */
.feature{position:absolute;top:3270px;width:325px;height:110px;display:flex;align-items:center;padding-left:62px;gap:16px}
.feature-dark{background:var(--ink);color:#fff}
.feature-lime{background:var(--lime);color:var(--ink)}
.feature h4{font-weight:800;font-size:16px;white-space:nowrap}
.feature p{font-size:12px;margin-top:3px;white-space:nowrap}

/* news */
.news-bg{position:absolute;left:0;top:3438px;width:1200px;height:522px;background:var(--news-bg)}
.news-img{position:absolute;width:257px;height:168px}
.date{position:absolute;width:38px;height:42px;background:var(--lime);text-align:center;color:var(--ink);font-weight:700;font-size:19px;line-height:22px;padding-top:4px}
.date small{display:block;font-size:8px;line-height:10px}
.news-text{position:absolute;width:220px}
.news-text h5{font-weight:600;font-size:14px;color:#222;white-space:nowrap}
.news-text p{font-size:11px;line-height:16px;color:#777;margin-top:10px}
.news-text a{display:block;font-size:10px;font-weight:700;color:#6fbf00;margin-top:8px;text-decoration:none}

/* newsletter */
.news-frame{position:absolute;left:145px;top:4006px;width:916px;height:228px;border:2px dotted #c7c7c7}
.signup{position:absolute;left:390px;top:4146px;width:424px;height:34px;background:var(--lime);display:flex;align-items:center;justify-content:space-between;padding:0 18px;font-size:12px;color:#333}

/* footer */
.site-footer{position:absolute;left:0;top:4280px;width:1200px;height:434px;background:var(--ink);color:#fff}
.foot-brand{position:absolute;left:93px;top:68px;font-weight:800;font-size:32px;display:flex;align-items:center;gap:10px}
.foot-brand .dot{width:14px;height:14px;background:var(--lime)}
.foot-about{position:absolute;left:93px;top:118px;width:470px;font-size:10.5px;line-height:16.5px;color:#ccc}
.foot-col{position:absolute;top:78px}
.foot-col h6{font-weight:700;font-size:17px;letter-spacing:.5px;white-space:nowrap}
.foot-col ul{list-style:none;margin-top:20px;font-size:10.5px;line-height:21.5px;color:#ccc;white-space:nowrap}
.social{position:absolute;top:275px;width:44px;height:44px;display:flex;align-items:center;justify-content:center;font-size:7px;font-weight:600;color:#fff}
.pay{position:absolute;top:275px;width:68px;height:42px;background:#fff;border-radius:3px;display:flex;align-items:center;justify-content:center;font-size:11px;font-weight:700;color:#2a3d8f}
.foot-rule{position:absolute;left:93px;top:346px;width:1014px;height:1px;background:#3a3a3a}
.copyright{position:absolute;left:93px;top:356px;font-size:10px;color:#888}
</style>
</head>
<body>

<!-- Hero background shapes -->
<svg class="hero-bg" viewBox="0 0 1200 1175" aria-hidden="true">
  <defs>
    <linearGradient id="darkFade" x1="0" y1="0" x2="1" y2="0">
      <stop offset="0" stop-color="#1b1b1b"/>
      <stop offset="1" stop-color="#242424"/>
    </linearGradient>
  </defs>
  <polygon points="0,0 1200,0 1200,880 0,1060" fill="url(#darkFade)"/>
  <polygon points="1200,160 1200,700 760,700" fill="#a3ef0a"/>
  <polygon points="0,898 420,790 420,860 0,1058" fill="#a3ef0a"/>
</svg>
<div class="photo" role="img" aria-label="Photo of a smiling woman in a sports top holding a lime shaker bottle" style="left:503px;top:70px;width:340px;height:616px;background:linear-gradient(180deg,#3a3a3a,#6b6560 60%,#2b2b2b)"></div>

<header class="site-header">
  <div class="brand"><span class="dot"></span>BRAMBLECREST</div>
  <nav class="main-nav">
    <span style="left:0">Home</span>
    <span style="left:77px">Clothing</span>
    <span style="left:168px">Supplement</span>
    <span style="left:283px">Blog</span>
    <span style="left:351px">Contact Us</span>
    <span style="left:448px;color:#888">|</span>
    <svg style="position:absolute;left:484px;top:-2px" width="18" height="16" viewBox="0 0 18 16"><path d="M1 2h3l2 8h9l2-6H5" fill="none" stroke="#fff" stroke-width="1.5"/><circle cx="7" cy="13" r="1.5" fill="#fff"/><circle cx="14" cy="13" r="1.5" fill="#fff"/></svg>
    <svg style="position:absolute;left:528px;top:-1px" width="14" height="14" viewBox="0 0 14 14"><circle cx="6" cy="6" r="4.5" fill="none" stroke="#fff" stroke-width="1.6"/><path d="M9.5 9.5l3.5 3.5" stroke="#fff" stroke-width="1.6"/></svg>
  </nav>
</header>

<h1 class="hero-title">BRAMBLECREST DEAL</h1>
<p class="hero-sub">Plus Extra 20%&nbsp; Off*</p>
<a class="btn-skew btn-lime" style="left:100px;top:443px;width:146px;height:36px"><span>Shop Now</span></a>

<!-- Promo grid -->
<div class="photo" role="img" aria-label="Photo of a man drinking from a blue sports bottle" style="left:93px;top:690px;width:304px;height:480px;background:linear-gradient(180deg,#c7ccd0,#8c949a)"></div>
<div class="promo promo-top">
  <h2>TOP 50</h2>
  <h3>Best Selling Supplements</h3>
  <p>Check Out Our Top Ten In Each Category</p>
  <a class="btn-skew btn-white" style="left:125px;top:152px;width:140px;height:32px"><span>Shop Now</span></a>
</div>
<div class="promo promo-sale">
  <h2>SALE &amp;<br>SPECIAL</h2>
  <a class="btn-skew btn-white" style="left:125px;top:152px;width:140px;height:32px"><span>Shop Now</span></a>
</div>
<div class="photo" role="img" aria-label="Photo of a woman with a towel holding a water bottle" style="left:803px;top:690px;width:304px;height:480px;background:linear-gradient(180deg,#e9e6e2,#b9aea6)"></div>

<!-- Newest products -->
<h2 class="section-title" style="top:1238px">EXPLORE THE NEWEST PRODUCTS</h2>
<p class="section-text" style="left:230px;top:1278px;width:740px">Lorem ipsum dolor sit amet, consectetur adipiscing elit. Nulla nisl libero, congue varius enim eu, maximus elementum nisl.<br>Etiam nulla tellus, iaculis ut eleifend vitae, condimentum vitae tortor.</p>
<div class="pager" style="left:1058px;top:1278px">
  <svg viewBox="0 0 22 22"><path d="M2 11h14M11 6l5 5-5 5M19 4v14" fill="none" stroke="#888" stroke-width="1.5"/></svg>
  <svg viewBox="0 0 22 22"><path d="M20 11H6M11 6l-5 5 5 5M3 4v14" fill="none" stroke="#555" stroke-width="1.5"/></svg>
</div>

<div class="card card-lg" style="left:93px;top:1344px">
  <span class="card-mark"></span>
  <div class="card-tools"><svg viewBox="0 0 18 18"><path d="M9 15S2 10.5 2 6.3A3.3 3.3 0 0 1 9 5a3.3 3.3 0 0 1 7 1.3C16 10.5 9 15 9 15z" fill="#ccc"/></svg><svg viewBox="0 0 18 18"><circle cx="8" cy="8" r="5" fill="none" stroke="#ccc" stroke-width="1.6"/><path d="M12 12l4 4" stroke="#ccc" stroke-width="1.6"/></svg><svg viewBox="0 0 18 18"><path d="M2 6h13l-3-3M16 12H3l3 3" fill="none" stroke="#ccc" stroke-width="1.6"/></svg></div>
  <div class="card-img" role="img" aria-label="Product photo of a protein tub beside dumbbells" style="background:linear-gradient(180deg,#3e4a6a,#1e2233)"></div>
  <div class="stars">★★★★★</div>
  <div class="card-name">WOMEN'S SPORT NUTRION</div>
  <div class="price">$18.99 <s>$29.50</s></div>
  <div class="card-desc">Lorem ipsum dolor sit amet, consectetur adipiscing</div>
  <a class="btn-skew btn-dark"><span>Shop Now</span></a>
</div>
<div class="card card-lg" style="left:439px;top:1344px">
  <span class="card-mark"></span>
  <div class="card-tools"><svg viewBox="0 0 18 18"><path d="M9 15S2 10.5 2 6.3A3.3 3.3 0 0 1 9 5a3.3 3.3 0 0 1 7 1.3C16 10.5 9 15 9 15z" fill="#ccc"/></svg><svg viewBox="0 0 18 18"><circle cx="8" cy="8" r="5" fill="none" stroke="#ccc" stroke-width="1.6"/><path d="M12 12l4 4" stroke="#ccc" stroke-width="1.6"/></svg><svg viewBox="0 0 18 18"><path d="M2 6h13l-3-3M16 12H3l3 3" fill="none" stroke="#ccc" stroke-width="1.6"/></svg></div>
  <div class="card-img" role="img" aria-label="Product photo of a woman in a grey and lime sports set" style="width:110px;background:linear-gradient(180deg,#d8c6b6,#9a9a9a 70%,#d6e84a)"></div>
  <div class="stars">★★★★★</div>
  <div class="card-name">WOMEN'S SPORT CLOTHS</div>
  <div class="price">$18.99 <s>$29.50</s></div>
  <div class="card-desc">Lorem ipsum dolor sit amet, consectetur adipiscing</div>
  <a class="btn-skew btn-dark"><span>Shop Now</span></a>
</div>
<div class="card card-lg" style="left:785px;top:1344px">
  <span class="card-mark"></span>
  <div class="card-tools"><svg viewBox="0 0 18 18"><path d="M9 15S2 10.5 2 6.3A3.3 3.3 0 0 1 9 5a3.3 3.3 0 0 1 7 1.3C16 10.5 9 15 9 15z" fill="#ccc"/></svg><svg viewBox="0 0 18 18"><circle cx="8" cy="8" r="5" fill="none" stroke="#ccc" stroke-width="1.6"/><path d="M12 12l4 4" stroke="#ccc" stroke-width="1.6"/></svg><svg viewBox="0 0 18 18"><path d="M2 6h13l-3-3M16 12H3l3 3" fill="none" stroke="#ccc" stroke-width="1.6"/></svg></div>
  <div class="card-img" role="img" aria-label="Product photo of a man in a black hooded track suit" style="width:110px;background:linear-gradient(180deg,#2a2a2a,#111)"></div>
  <div class="stars">★★★★★</div>
  <div class="card-name">WOMEN'S SPORT NUTRION</div>
  <div class="price">$18.99 <s>$29.50</s></div>
  <div class="card-desc">Lorem ipsum dolor sit amet, consectetur adipiscing</div>
  <a class="btn-skew btn-dark"><span>Shop Now</span></a>
</div>

<!-- Supplement section -->
<div class="abs" style="left:0;top:1838px;width:503px;height:476px;background:var(--mist)"></div>
<div class="photo" role="img" aria-label="Photo of a shirtless athlete pointing at a lime supplement tub" style="left:110px;top:1820px;width:440px;height:494px;background:linear-gradient(160deg,#d6a584,#a36f52 70%,#d7ef4a)"></div>
<h2 class="section-title compact" style="left:582px;width:545px;top:1834px">BRAMBLECREST SUPPLEMENT</h2>
<div class="tabs" style="left:622px;top:1876px"><b>Protein</b><i>/</i>Pre-Workout<i>/</i>Post-Workout<i>/</i>Fat Burners<i>/</i>Creatine</div>

<div class="card card-sm" style="left:602px;top:1915px">
  <span class="card-mark"></span>
  <div class="card-tools"><svg viewBox="0 0 18 18"><path d="M9 15S2 10.5 2 6.3A3.3 3.3 0 0 1 9 5a3.3 3.3 0 0 1 7 1.3C16 10.5 9 15 9 15z" fill="#ccc"/></svg><svg viewBox="0 0 18 18"><circle cx="8" cy="8" r="5" fill="none" stroke="#ccc" stroke-width="1.6"/><path d="M12 12l4 4" stroke="#ccc" stroke-width="1.6"/></svg></div>
  <div class="card-img" role="img" aria-label="Product photo of a black supplement jar and dumbbell" style="background:linear-gradient(180deg,#2c2c2c,#0f0f0f)"></div>
  <div class="stars">★★★★★</div>
  <div class="card-name">FAT BURNER SUPPLEMENT</div>
  <div class="price">$18.99 <s>$29.50</s></div>
  <div class="card-desc">Lorem ipsum dolor sit amet, consectetur</div>
  <a class="btn-skew btn-dark"><span>Shop Now</span></a>
</div>
<div class="card card-sm" style="left:862px;top:1915px">
  <span class="card-mark"></span>
  <div class="card-tools"><svg viewBox="0 0 18 18"><path d="M9 15S2 10.5 2 6.3A3.3 3.3 0 0 1 9 5a3.3 3.3 0 0 1 7 1.3C16 10.5 9 15 9 15z" fill="#ccc"/></svg><svg viewBox="0 0 18 18"><circle cx="8" cy="8" r="5" fill="none" stroke="#ccc" stroke-width="1.6"/><path d="M12 12l4 4" stroke="#ccc" stroke-width="1.6"/></svg></div>
  <div class="card-img" role="img" aria-label="Product photo of a black supplement jar and dumbbell" style="background:linear-gradient(180deg,#2c2c2c,#0f0f0f)"></div>
  <div class="stars">★★★★★</div>
  <div class="card-name">CLA SUPPLEMENT</div>
  <div class="price">$18.99 <s>$29.50</s></div>
  <div class="card-desc">Lorem ipsum dolor sit amet, consectetur</div>
  <a class="btn-skew btn-dark"><span>Shop Now</span></a>
</div>
<div class="pager" style="left:1058px;top:2251px">
  <svg viewBox="0 0 22 22"><path d="M2 11h14M11 6l5 5-5 5M19 4v14" fill="none" stroke="#888" stroke-width="1.5"/></svg>
  <svg viewBox="0 0 22 22"><path d="M20 11H6M11 6l-5 5 5 5M3 4v14" fill="none" stroke="#555" stroke-width="1.5"/></svg>
</div>

<!-- Deal band -->
<svg class="deal-band" viewBox="0 0 1200 338" aria-hidden="true">
  <rect width="1200" height="338" fill="#1e1e1e"/>
  <polygon points="723,0 1200,0 1200,338 622,338" fill="#a3ef0a"/>
  <line x1="0" y1="336" x2="1200" y2="336" stroke="#555" stroke-dasharray="3 3"/>
</svg>
<div class="photo" role="img" aria-label="Photo of a woman in black activewear seated stretching" style="left:640px;top:2296px;width:430px;height:384px;background:linear-gradient(180deg,#3a3a3a,#1c1c1c)"></div>
<p class="band-text">Etiam nulla tellus, iaculis ut eleifend<br>vitae, condimentum vitae tortor.</p>
<p class="band-big">Flat 50% off</p>
<a class="btn-skew btn-lime" style="left:100px;top:2533px;width:146px;height:36px"><span>Shop Now</span></a>

<!-- Clothing section -->
<div class="abs" style="left:699px;top:2734px;width:501px;height:476px;background:var(--mist)"></div>
<div class="photo" role="img" aria-label="Photo of a muscular man opening a grey hooded jacket" style="left:600px;top:2711px;width:430px;height:499px;background:linear-gradient(180deg,#9a9a9a,#b88a6c 45%,#2a2a2a)"></div>
<h2 class="section-title compact" style="left:73px;width:547px;top:2730px">BRAMBLECREST CLOTHING</h2>
<div class="tabs" style="left:97px;top:2774px"><b>Men's Clothing</b><i>/</i>Women's Clothing<i>/</i>Exclusives<i>/</i>New Arrivals<i>/</i>Hats</div>

<div class="card card-sm" style="left:93px;top:2813px">
  <span class="card-mark"></span>
  <div class="card-tools"><svg viewBox="0 0 18 18"><path d="M9 15S2 10.5 2 6.3A3.3 3.3 0 0 1 9 5a3.3 3.3 0 0 1 7 1.3C16 10.5 9 15 9 15z" fill="#ccc"/></svg><svg viewBox="0 0 18 18"><circle cx="8" cy="8" r="5" fill="none" stroke="#ccc" stroke-width="1.6"/><path d="M12 12l4 4" stroke="#ccc" stroke-width="1.6"/></svg></div>
  <div class="card-img" role="img" aria-label="Product photo of a man in a navy tank top" style="width:80px;background:linear-gradient(180deg,#1f2b4c,#2a2a2a)"></div>
  <div class="stars">★★★★★</div>
  <div class="card-name">FAT BURNER SUPPLEMENT</div>
  <div class="price">$18.99 <s>$29.50</s></div>
  <div class="card-desc">Lorem ipsum dolor sit amet, consectetur</div>
  <a class="btn-skew btn-dark"><span>Shop Now</span></a>
</div>
<div class="card card-sm" style="left:355px;top:2813px">
  <span class="card-mark"></span>
  <div class="card-tools"><svg viewBox="0 0 18 18"><path d="M9 15S2 10.5 2 6.3A3.3 3.3 0 0 1 9 5a3.3 3.3 0 0 1 7 1.3C16 10.5 9 15 9 15z" fill="#ccc"/></svg><svg viewBox="0 0 18 18"><circle cx="8" cy="8" r="5" fill="none" stroke="#ccc" stroke-width="1.6"/><path d="M12 12l4 4" stroke="#ccc" stroke-width="1.6"/></svg></div>
  <div class="card-img" role="img" aria-label="Product photo of a man in a grey sleeveless hoodie" style="width:80px;background:linear-gradient(180deg,#a8a8a8,#6e6e6e)"></div>
  <div class="stars">★★★★★</div>
  <div class="card-name">CLA SUPPLEMENT</div>
  <div class="price">$18.99 <s>$29.50</s></div>
  <div class="card-desc">Lorem ipsum dolor sit amet, consectetur</div>
  <a class="btn-skew btn-dark"><span>Shop Now</span></a>
</div>
<div class="pager" style="left:93px;top:3148px">
  <svg viewBox="0 0 22 22"><path d="M2 11h14M11 6l5 5-5 5M19 4v14" fill="none" stroke="#888" stroke-width="1.5"/></svg>
  <svg viewBox="0 0 22 22"><path d="M20 11H6M11 6l-5 5 5 5M3 4v14" fill="none" stroke="#555" stroke-width="1.5"/></svg>
</div>

<!-- Features -->
<div class="feature feature-dark" style="left:93px">
  <svg width="62" height="38" viewBox="0 0 62 38" aria-hidden="true"><rect x="2" y="6" width="36" height="22" fill="#f8524d"/><path d="M38 12h12l8 8v8H38z" fill="#3b8ede"/><circle cx="14" cy="31" r="5" fill="#fff" stroke="#333" stroke-width="2"/><circle cx="48" cy="31" r="5" fill="#fff" stroke="#333" stroke-width="2"/></svg>
  <div><h4>FREE SHIPPING*</h4><p>On order over $199.</p></div>
</div>
<div class="feature feature-lime" style="left:439px">
  <svg width="56" height="56" viewBox="0 0 56 56" aria-hidden="true"><circle cx="28" cy="28" r="25" fill="#f2b51c" stroke="#c8561f" stroke-width="3"/><circle cx="28" cy="28" r="15" fill="#f7d55a"/></svg>
  <div><h4>100% MONEY BACK*</h4><p>Within 30 Days after delivery</p></div>
</div>
<div class="feature feature-dark" style="left:783px">
  <svg width="50" height="46" viewBox="0 0 50 46" aria-hidden="true"><path d="M8 24a17 17 0 0 1 34 0" fill="none" stroke="#fff" stroke-width="3"/><rect x="4" y="22" width="8" height="14" rx="2" fill="#a3ef0a"/><rect x="38" y="22" width="8" height="14" rx="2" fill="#a3ef0a"/><path d="M42 36q0 6-10 6" fill="none" stroke="#fff" stroke-width="2"/></svg>
  <div><h4>SUPPORT 24/7*</h4><p>We can help You online</p></div>
</div>

<!-- News -->
<div class="news-bg"></div>
<h2 class="section-title" style="top:3484px">BRAMBLECREST NEWS</h2>

<div class="news-img" role="img" aria-label="Photo of an athlete scooping protein powder" style="left:93px;top:3539px;background:linear-gradient(135deg,#5a5a5a,#b98a6c)"></div>
<div class="date" style="left:318px;top:3528px">21<small>MAY</small></div>
<div class="news-text" style="left:379px;top:3578px"><h5>Donec quam nunc, vulputate</h5><p>Donec cursus massa mi. Sed et condimentum orci, vel gravida eros. Nulla sit amet euismod libero.</p><a>Read More ›</a></div>

<div class="news-img" role="img" aria-label="Photo of a woman rolling out a yoga mat" style="left:609px;top:3539px;background:linear-gradient(135deg,#b7b7b7,#6c8ca6)"></div>
<div class="date" style="left:834px;top:3528px">21<small>MAY</small></div>
<div class="news-text" style="left:893px;top:3578px"><h5>Donec quam nunc, vulputate</h5><p>Donec cursus massa mi. Sed et condimentum orci, vel gravida eros. Nulla sit amet euismod libero.</p><a>Read More ›</a></div>

<div class="news-text" style="left:93px;top:3773px"><h5>Donec quam nunc, vulputate</h5><p>Donec cursus massa mi. Sed et condimentum orci, vel gravida eros. Nulla sit amet euismod libero.</p><a>Read More ›</a></div>
<div class="news-img" role="img" aria-label="Photo of two athletes doing a partner workout on the floor" style="left:337px;top:3737px;background:linear-gradient(135deg,#2e2e2e,#555)"></div>
<div class="date" style="left:330px;top:3726px">21<small>MAY</small></div>

<div class="news-text" style="left:609px;top:3773px"><h5>Donec quam nunc, vulputate</h5><p>Donec cursus massa mi. Sed et condimentum orci, vel gravida eros. Nulla sit amet euismod libero.</p><a>Read More ›</a></div>
<div class="news-img" role="img" aria-label="Photo of a man resting with a towel in an orange gym" style="left:851px;top:3737px;background:linear-gradient(90deg,#d6581f,#3a3a3a 60%,#d6581f)"></div>
<div class="date" style="left:844px;top:3726px">21<small>MAY</small></div>

<!-- Newsletter -->
<div class="news-frame"></div>
<h2 class="section-title" style="top:4049px">NEWSLETTER SUBSCRIPTION</h2>
<p class="section-text" style="left:300px;top:4095px;width:600px">Lorem ipsum dolor sit amet, consectetur adipiscing elit. Nulla nisl libero, congue varius enim eu,<br>maximus elementum nisl.</p>
<div class="signup"><span>Enter Your Name</span><svg width="14" height="10" viewBox="0 0 14 10"><path d="M1 5h11M8 1l4 4-4 4" fill="none" stroke="#222" stroke-width="1.5"/></svg></div>

<!-- Footer -->
<footer class="site-footer">
  <div class="foot-brand"><span class="dot"></span>BRAMBLECREST</div>
  <p class="foot-about">Donec cursus massa mi. Sed et condimentum orci, vel gravida eros. Nulla sit amet euismod libero. Nullam blandit sem at eros feugiat rutrum. Donec commodo gravida mollis. Suspendisse blandit efficitur tellus. Donec commodo gravida mollis. Suspendisse blandit efficitur tellus, vitae blandit elit hendrerit non. Cras consequat posuere convallis.</p>
  <div class="foot-col" style="left:629px"><h6>ABOUT</h6><ul><li>About Us</li><li>Shopping Guide</li><li>Delivery Information</li><li>Privacy Policy</li><li>Our Store</li></ul></div>
  <div class="foot-col" style="left:816px"><h6>ACCOUNT</h6><ul><li>My Account</li><li>Wishlist</li><li>Order Tracking</li><li>Shipping Info</li><li>Return Policy</li></ul></div>
  <div class="foot-col" style="left:1000px"><h6>NEED HELP?</h6><ul><li>Help Center</li><li>Email Support</li><li>Live Chat</li><li>Gift Certificates</li><li>Send Us Feedback</li></ul></div>

  <span class="social" style="left:93px;background:#3b5998">Facet</span>
  <span class="social" style="left:150px;background:#2d9fe0">Chirpline</span>
  <span class="social" style="left:207px;background:#d92b2b">Tubecast</span>
  <span class="social" style="left:264px;background:#3f729b">Snapframe</span>

  <span class="pay" style="left:730px">Veyra</span>
  <span class="pay" style="left:808px">Meridian</span>
  <span class="pay" style="left:886px">Amberlane</span>
  <span class="pay" style="left:964px">Paytide</span>
  <span class="pay" style="left:1042px;width:65px">Dovecard</span>

  <div class="foot-rule"></div>
  <p class="copyright">Bramblecrest Apparel and Nutrition © 2019 All Rights Reserved.</p>
</footer>

</body>
</html>
```